M25 Billboard Advert Required Please

I need an advert for a motorway Billboard on the M25 , the advert should show the following in big letters:
GUTTER CLEANING
DALRYNFLUES.COM and a small logo off to the side (Our logo is attached)

The printer has requested the following (Important please) the advert has to be
pdf file / 300 dpi/landscape orientation / scaled to a minimum 25% advert size ( this particular site is 22ft x 10ft so 25% of this please). Please also make sure that the artwork is embedded and outlined correctly if this is incorrect it will affect the printing of the banner.

Target Market(s)

General Public

Industry/Entity Type

Gutter Cleaning

Requirements
Should not have
• No Change to our Logo

```html
<!DOCTYPE html>
<html lang="en">
<head>
<meta charset="utf-8">
<title>Dalryn Flues – Gutter Cleaning Billboard</title>
<link rel="stylesheet" href="https://fonts.googleapis.com/css2?family=Montserrat:wght@500;600;700&family=Open+Sans:wght@600&display=swap">
<style>
  :root {
    --page-bg: #231f20;
    --ink: #0a0a0a;
    --panel-black: #000000;
    --brand-red: #e8001c;
    --band-edge: #cdcdcd;
    --band-mid: #f5f5f5;
  }
  html, body {
    margin: 0;
    padding: 0;
    width: 1200px;
    height: 1200px;
    overflow: hidden;
    background: var(--page-bg);
  }
  .billboard {
    position: absolute;
    left: 40px;
    top: 345px;
    width: 1120px;
    height: 509px;
  }
  .billboard svg {
    display: block;
    width: 1120px;
    height: 509px;
  }
  .brand-name {
    font-family: "Montserrat", sans-serif;
    font-weight: 700;
    font-size: 40px;
    fill: var(--ink);
  }
  .tagline {
    font-family: "Open Sans", sans-serif;
    font-weight: 600;
    font-size: 17px;
    fill: #222222;
  }
  .headline {
    font-family: "Montserrat", sans-serif;
    font-weight: 700;
    fill: var(--brand-red);
  }
  .headline-main { font-size: 214px; }
  .headline-sub { font-size: 112px; font-weight: 600; }
  .web-address {
    font-family: "Montserrat", sans-serif;
    font-weight: 500;
    font-size: 54px;
    fill: var(--ink);
  }
  .web-address .domain {
    font-weight: 700;
    fill: var(--brand-red);
  }
</style>
</head>
<body>
  <div class="billboard">
    <svg viewBox="0 0 1120 509" xmlns="http://www.w3.org/2000/svg" aria-label="Dalryn Flues gutter cleaning billboard">
      <defs>
        <linearGradient id="bandSheen" x1="0" y1="0" x2="1" y2="0">
          <stop offset="0" stop-color="var(--band-edge)"/>
          <stop offset="0.5" stop-color="var(--band-mid)"/>
          <stop offset="1" stop-color="var(--band-edge)"/>
        </linearGradient>
      </defs>

      <!-- brand band -->
      <rect class="brand-band" x="0" y="0" width="1120" height="129" fill="url(#bandSheen)"/>
      <rect class="brand-square" x="418" y="42" width="30" height="30" fill="var(--ink)"/>
      <text class="brand-name" x="460" y="71">Dalryn Flues</text>
      <text class="tagline" x="560" y="113" text-anchor="middle">Clean gutters protect your property</text>

      <!-- headline panel -->
      <rect class="headline-panel" x="0" y="129" width="1120" height="302" fill="var(--panel-black)"/>
      <text class="headline headline-main" x="150" y="311" textLength="822" lengthAdjust="spacing">GUTTER</text>
      <text class="headline headline-sub" x="150" y="408" textLength="822" lengthAdjust="spacing">CLEANING</text>

      <!-- address band -->
      <rect class="address-band" x="0" y="431" width="1120" height="78" fill="url(#bandSheen)"/>
      <text class="web-address" x="158" y="488" textLength="806" lengthAdjust="spacing">WWW.<tspan class="domain">DALRYNFLUES</tspan>.COM</text>
    </svg>
  </div>
</body>
</html>
```